Telecommunications Company needs a business card design

We are looking for a sleek, professional and modern business card design based off our new logo. Will look at both light and dark options. On some designs please provide a small space for a QR code

Target Market(s)

B2B clients in Australia

Contact Information for Business Card

Name, Position, Brisbane (head) office, Phone number, email address, QR code (link to our website kzcommunications.com.au

Colors
0054AA
0677BA
7BADD7
CADEEF
E8F1F8
0094D4
00A9DD
6FCCEA
C7EBF8
E9F6FB
00AB8E
00BBA5
67D7C9
C6EFE9
E9F9F6

```html
<!DOCTYPE html>
<html lang="en">
<head>
<meta charset="utf-8">
<title>KZ Communications – Business Card</title>
<link href="https://fonts.googleapis.com/css2?family=Arimo:wght@400;700&display=swap" rel="stylesheet">
<style>
  :root {
    --bg: #e4e4e2;
    --card: #2e2e31;
    --card-back: #2b2b2e;
    --ink: #f4f4f4;
    --ink-soft: #d9d9d9;
    --blue-deep: #0054AA;
    --blue: #0677BA;
    --sky: #00A9DD;
    --teal: #00BBA5;
    --teal-deep: #00AB8E;
    --emboss: #3c3c40;
  }
  * { box-sizing: border-box; margin: 0; padding: 0; }
  html, body {
    width: 1200px; height: 801px; overflow: hidden;
    background: var(--bg);
    font-family: "Arimo", Arial, sans-serif;
  }
  .canvas {
    width: 1200px; height: 801px;
    display: flex; align-items: center; justify-content: center; gap: 50px;
  }
  .card {
    position: relative;
    width: 540px; height: 310px;
    border-radius: 3px;
    overflow: hidden;
    box-shadow: 0 6px 18px rgba(0,0,0,.18);
  }

  /* Front */
  .card--front { background: var(--card); color: var(--ink); }
  .brand {
    position: absolute; top: 46px; right: 44px;
    display: flex; align-items: center; gap: 10px;
    font-weight: 700; font-size: 22px; letter-spacing: 2px;
    text-transform: uppercase; color: var(--ink);
  }
  .brand__square { width: 14px; height: 14px; background: var(--sky); }
  .person {
    position: absolute; left: 64px; top: 116px;
  }
  .person__name {
    font-weight: 700; font-size: 25px; letter-spacing: .5px;
    text-transform: uppercase;
    background: linear-gradient(90deg, var(--blue) 0%, var(--sky) 55%, var(--teal) 100%);
    -webkit-background-clip: text; background-clip: text; color: transparent;
  }
  .person__role { font-size: 15px; color: var(--ink); margin-top: 2px; }
  .divider {
    position: absolute; left: 64px; right: 56px; top: 176px;
    height: 1px; background: var(--ink-soft);
  }
  .contacts {
    position: absolute; left: 64px; top: 192px;
    list-style: none; font-size: 14px; line-height: 24px;
    white-space: nowrap;
  }
  .contacts li { display: flex; align-items: center; gap: 10px; }
  .contacts svg { width: 13px; height: 13px; fill: var(--sky); flex: none; }
  .address {
    position: absolute; right: 56px; top: 196px;
    font-style: normal; font-size: 14px; line-height: 26px;
    text-align: right; color: var(--ink); white-space: nowrap;
  }
  .tab {
    position: absolute; left: 0; top: 216px;
    width: 10px; height: 30px; border-radius: 0 4px 4px 0;
    background: linear-gradient(180deg, var(--teal), var(--sky));
  }
  .edge-band {
    position: absolute; left: 0; right: 0; bottom: 0; height: 7px;
    background: linear-gradient(90deg, var(--blue) 0%, var(--sky) 50%, var(--teal) 100%);
  }

  /* Back */
  .card--back {
    background: var(--card-back);
    display: flex; align-items: center; justify-content: center;
  }
  .back-mark {
    font-weight: 700; font-size: 30px; letter-spacing: 4px;
    text-transform: uppercase; color: var(--emboss);
  }
</style>
</head>
<body>
<main class="canvas">
  <section class="card card--front" aria-label="Business card front">
    <div class="brand"><span class="brand__square"></span>KZ Communications</div>

    <div class="person">
      <h1 class="person__name">Daniel Mercer</h1>
      <p class="person__role">Manager</p>
    </div>

    <div class="divider"></div>

    <ul class="contacts">
      <li>
        <svg viewBox="0 0 24 24" aria-hidden="true"><path d="M6.6 10.8a15.1 15.1 0 0 0 6.6 6.6l2.2-2.2c.3-.3.7-.4 1-.2 1.1.4 2.3.6 3.6.6.6 0 1 .4 1 1V20c0 .6-.4 1-1 1A17 17 0 0 1 3 4c0-.6.4-1 1-1h3.5c.6 0 1 .4 1 1 0 1.3.2 2.5.6 3.6.1.3 0 .7-.2 1z"/></svg>
        07 3555 0192
      </li>
      <li>
        <svg viewBox="0 0 24 24" aria-hidden="true"><path d="M2 5h20v14H2zm2 2v.5l8 5 8-5V7l-8 5z"/></svg>
        daniel@kzcommunications.com.au
      </li>
      <li>
        <svg viewBox="0 0 24 24" aria-hidden="true"><path d="M12 2a10 10 0 1 0 0 20 10 10 0 0 0 0-20zm6.9 6h-3a15 15 0 0 0-1.3-3.9A8 8 0 0 1 18.9 8zM12 4c.8 1.2 1.5 2.5 1.9 4h-3.8c.4-1.5 1.1-2.8 1.9-4zM4.3 14a8 8 0 0 1 0-4h3.4a16 16 0 0 0 0 4zm.8 2h3a15 15 0 0 0 1.3 3.9A8 8 0 0 1 5.1 16zm3-8h-3a8 8 0 0 1 4.3-3.9C8.8 5.3 8.4 6.6 8.1 8zM12 20c-.8-1.2-1.5-2.5-1.9-4h3.8c-.4 1.5-1.1 2.8-1.9 4zm2.3-6H9.7a14 14 0 0 1 0-4h4.6a14 14 0 0 1 0 4zm.3 5.9c.6-1.2 1-2.5 1.3-3.9h3a8 8 0 0 1-4.3 3.9zm1.7-5.9a16 16 0 0 0 0-4h3.4a8 8 0 0 1 0 4z"/></svg>
        www.kzcommunications.com.au
      </li>
    </ul>

    <address class="address">
      Level 4, 120 Harbour St<br>
      Brisbane<br>
      QLD 4000
    </address>

    <span class="tab"></span>
    <span class="edge-band"></span>
  </section>

  <section class="card card--back" aria-label="Business card back">
    <p class="back-mark">KZ Communications</p>
  </section>
</main>
</body>
</html>
```